Book cover needed for self help business book

Book cover needed and I will provide back cover blurb and barcode to the winning designer. Book may be too small for spine, but I will give you the page number details to confirm. Book information below:

Title: Nine Winters a Trader
Subtitle: Proven Market Methods That Keep Paying Off Now
Author: Maribel Okonte

Design should be clean, modern, and bold—something that appeals to everyday entrepreneurs and resellers. The cover should reflect grit, real-world hustle, and long-term wisdom without looking overly corporate or flashy. I am open to your creative ideas.

I am open to modern designs, but also designs of rugged old covers that simulate a book that may have aged over the years.

I prefer not to have pictures or silhouettes of people

Requirements
Nice to have
• I am open to modern designs, but also designs of rugged old covers that simulate a book that may have aged over the years.
Should not have
• Pictures or silhouettes of people

```html
<!DOCTYPE html>
<html lang="en">
<head>
<meta charset="utf-8">
<title>Nine Winters a Trader — Cover</title>
<link rel="stylesheet" href="https://fonts.googleapis.com/css2?family=Montserrat:wght@800;900&family=Roboto+Slab:wght@400;500&family=Fira+Sans+Condensed:ital,wght@0,600;0,700;1,800&display=swap">
<style>
  :root {
    --page: #ffffff;
    --stone-light: #f1f1ef;
    --stone-mid: #dcdcd8;
    --stone-warm: #d6cdb8;
    --ink-dark: #352f28;
    --navy: #0f2a7a;
    --green: #137012;
    --leather: #8a5a2e;
    --leather-deep: #5e3a1c;
    --tile: #d9c8ae;
  }
  * { margin: 0; padding: 0; box-sizing: border-box; }
  html, body { width: 1200px; height: 1200px; overflow: hidden; background: var(--page); }
  .cover {
    position: absolute; left: 240px; top: 60px; width: 720px; height: 1080px; overflow: hidden;
    background:
      linear-gradient(90deg, transparent 0 6%, rgba(214,205,184,.35) 7%, transparent 9% 24%, rgba(200,200,196,.4) 25%, transparent 27% 58%, rgba(214,205,184,.3) 60%, transparent 62% 88%, rgba(200,200,196,.35) 90%, transparent 92%),
      linear-gradient(170deg, var(--stone-light), var(--stone-mid) 55%, var(--stone-light));
  }
  .feature-photo { position: absolute; left: 0; top: 0; width: 720px; height: 1080px; }
  .title-word { position: absolute; color: var(--ink-dark); line-height: 1; white-space: nowrap; }
  .title-number { right: 340px; top: 60px; font: 900 82px/1 "Montserrat", sans-serif; letter-spacing: -5px; }
  .title-caps { right: 336px; top: 150px; font: 900 70px/1 "Montserrat", sans-serif; letter-spacing: -5px; }
  .title-article { left: 396px; top: 56px; font: 500 82px/1 "Roboto Slab", serif; }
  .title-noun { left: 392px; top: 128px; font: 500 96px/1 "Roboto Slab", serif; letter-spacing: -2px; }
  .subtitle { position: absolute; left: 58px; top: 520px; white-space: nowrap; font-family: "Fira Sans Condensed", sans-serif; }
  .subtitle-lead { display: block; color: var(--navy); font-weight: 600; font-size: 84px; line-height: 1.05; letter-spacing: -1px; }
  .subtitle-key { display: block; color: var(--green); font-weight: 700; font-size: 132px; line-height: .95; letter-spacing: 1px; }
  .subtitle-mid { display: block; color: var(--green); font-weight: 700; font-size: 92px; line-height: 1; }
  .subtitle-tail { display: block; font-size: 52px; line-height: 1.1; }
  .subtitle-tail .soft { color: var(--green); font-weight: 600; }
  .subtitle-tail .strong { color: var(--navy); font-weight: 800; font-style: italic; }
  .author { position: absolute; left: 0; width: 720px; top: 968px; text-align: center; color: var(--ink-dark); font: 400 68px/1 "Roboto Slab", serif; letter-spacing: 1px; }
</style>
</head>
<body>
  <main class="cover">
    <svg class="feature-photo" viewBox="0 0 720 1080" role="img" aria-label="Photo of a leather tool belt holding pliers, a tape measure and a hammer beside stacks of banknotes on a kitchen counter">
      <defs>
        <linearGradient id="photoTone" x1="0" y1="0" x2="0" y2="1">
          <stop offset="0" stop-color="var(--tile)"/>
          <stop offset=".35" stop-color="var(--leather)"/>
          <stop offset=".7" stop-color="var(--leather-deep)"/>
          <stop offset="1" stop-color="#cfc8b8"/>
        </linearGradient>
        <linearGradient id="textVeil" x1="0" y1="0" x2="1" y2="0">
          <stop offset="0" stop-color="#f3f3f1" stop-opacity=".95"/>
          <stop offset=".7" stop-color="#f3f3f1" stop-opacity=".8"/>
          <stop offset="1" stop-color="#f3f3f1" stop-opacity="0"/>
        </linearGradient>
      </defs>
      <polygon points="168,212 720,238 720,848 160,838" fill="url(#photoTone)"/>
      <rect x="40" y="500" width="560" height="420" fill="url(#textVeil)"/>
    </svg>

    <h1>
      <span class="title-word title-number">Nine</span>
      <span class="title-word title-caps">WINTERS</span>
      <span class="title-word title-article">a</span>
      <span class="title-word title-noun">Trader</span>
    </h1>

    <p class="subtitle">
      <span class="subtitle-lead">Proven Market</span>
      <span class="subtitle-key">METHODS</span>
      <span class="subtitle-mid">THAT KEEP</span>
      <span class="subtitle-tail"><span class="soft">paying</span> <span class="strong">Off Now</span></span>
    </p>

    <p class="author">Maribel Okonte</p>
  </main>
</body>
</html>
```